Production Company Needs Poster for Feature Film

We need a poster for a thriller/horror film that will be released on Vuremix. We would like something that is 1- simple and 2- looks professionally done.

In the movie Jo (female lead) finds out the devil wants to use her suffering (loss of entire family) to open a portal and escape into our world. If the devil gets loose he will kill millions. Jo is befriended by Mark (male lead) and Mike (supporting male lead). They are a team of sufferer hunters who find people like Jo (the sufferer) and help them close the portal before the devil escapes. In order to close the portal they must find 2 objects and destroy them. During their hunt Mike is accidently killed by Mark while they are saving Jo from the devil's underlings. Mark is then captured and must be rescued by Jo. It turns out that Mike was previously captured and tortured by the devil until he agreed to work for him. Mike is planning on handing Jo over to the devil, but must be stopped by Mark and Jo.

The trailer can be found at https://www.clipvane.example/watch?v=k-tQzRB8Mun

Attached are a number of uncorrected pictures of the 3 leads. Each picture is labeled with the name of the characters from left to right. Note it is NOT a requirement to use these pictures. They are provided if the designer desires to use them.

Target Market(s)

Independent horror/thriller movie fans. 18-30 years old, technically savvy, consumes much of their content on their phone or computer.

Industry/Entity Type

It Company

Requirements
Must have
• The poster must include the title of the movie "The Hollowing" in large, legible print. Since the poster is for Vuremix it is important that the words and the theme are easily understood when it is shown as a thumbnail on the Vuremix website on a computer of phone.
• The final image needs to conform to the requirements below.
• - RGB color space with 1400x2100 pixels minimum size (2:3 ratio) 
Nice to have
• Custom lettering that fits the theme of the poster.
• Beyond that we are purposely not providing additional artistic input/design requirements. We want to see maximum creativity from the designers and want a range of options.
Should not have
• It should not have small lettering or details that won't translate well when the image is displayed as a thumbnail. Do not use a standard font (serif, times new roman...).

```html
<!DOCTYPE html>
<html lang="en">
<head>
<meta charset="utf-8">
<title>The Hollowing — Poster</title>
<link rel="stylesheet" href="https://fonts.googleapis.com/css2?family=Antonio:wght@600&family=Oswald:wght@500&display=swap">
<style>
  :root {
    --bg: #0a060c;
    --ink: #f4f0f6;
    --credit: #ece6ef;
    --glow: rgba(170, 110, 210, 0.7);
    --portrait-light: #cfc6d6;
    --portrait-mid: #8a72a0;
    --portrait-shadow: #3c2a48;
    --ghost: #2a1c32;
    --pattern: #241628;
  }
  html, body {
    margin: 0;
    padding: 0;
    width: 800px;
    height: 1200px;
    overflow: hidden;
    background: var(--bg);
  }
  .poster {
    position: relative;
    width: 800px;
    height: 1200px;
    background: var(--bg);
    overflow: hidden;
    font-family: "Oswald", sans-serif;
  }
  .portrait {
    position: absolute;
    left: 0;
    top: 140px;
    width: 560px;
    height: 480px;
  }
  .portrait-ghost {
    position: absolute;
    border-radius: 45% 45% 42% 42%;
    filter: blur(14px);
  }
  .portrait-ghost.is-left {
    left: -30px;
    top: 90px;
    width: 150px;
    height: 320px;
    background: radial-gradient(ellipse at 60% 45%, #4a3656 0%, var(--ghost) 60%, transparent 100%);
  }
  .portrait-ghost.is-right {
    left: 330px;
    top: 40px;
    width: 210px;
    height: 400px;
    background: radial-gradient(ellipse at 45% 45%, #4e3a5c 0%, var(--ghost) 60%, transparent 100%);
  }
  .portrait-main {
    position: absolute;
    left: 95px;
    top: 20px;
    width: 275px;
    height: 420px;
    border-radius: 42% 42% 38% 38% / 34% 34% 40% 40%;
    background:
      radial-gradient(ellipse 120px 170px at 55% 42%, var(--portrait-light) 0%, #b3a6c0 40%, var(--portrait-mid) 72%, var(--portrait-shadow) 100%);
    filter: blur(9px);
    opacity: 0.92;
  }
  .backdrop-pattern {
    position: absolute;
    left: 0;
    top: 820px;
    width: 800px;
    height: 380px;
    background:
      radial-gradient(ellipse 420px 200px at 30% 70%, rgba(70, 44, 80, 0.35) 0%, transparent 100%),
      linear-gradient(to bottom, transparent 0%, var(--pattern) 30%, #1a0f1d 100%);
  }
  .cast {
    position: absolute;
    top: 50px;
    left: 0;
    width: 800px;
    margin: 0;
    padding: 0;
    list-style: none;
  }
  .cast-name {
    position: absolute;
    transform: translateX(-50%);
    white-space: nowrap;
    font-size: 18px;
    font-variant: small-caps;
    letter-spacing: 0.4px;
    color: var(--credit);
  }
  .title {
    position: absolute;
    left: 0;
    top: 0;
    width: 800px;
    height: 1200px;
    overflow: visible;
  }
  .title text {
    font-family: "Antonio", sans-serif;
    font-weight: 600;
    fill: var(--ink);
    filter: drop-shadow(0 0 5px var(--glow)) drop-shadow(0 2px 2px rgba(0,0,0,0.6));
  }
  .writers {
    position: absolute;
    left: 0;
    width: 800px;
    top: 1100px;
    margin: 0;
    text-align: center;
    font-size: 17px;
    font-variant: small-caps;
    letter-spacing: 0.4px;
    color: var(--credit);
  }
</style>
</head>
<body>
  <main class="poster">
    <div class="portrait" role="img" aria-label="Blurred, purple-toned portrait of the female lead with two ghostly doubled faces beside her">
      <div class="portrait-ghost is-left"></div>
      <div class="portrait-ghost is-right"></div>
      <div class="portrait-main"></div>
    </div>
    <div class="backdrop-pattern" role="img" aria-label="Dark purple damask fabric texture"></div>

    <ul class="cast">
      <li class="cast-name" style="left:206px">Maren Voss</li>
      <li class="cast-name" style="left:405px">Tobin Hale</li>
      <li class="cast-name" style="left:603px">Casius Wren</li>
    </ul>

    <svg class="title" viewBox="0 0 800 1200" aria-label="The Hollowing">
      <text x="492" y="588" font-size="190" textLength="176" lengthAdjust="spacingAndGlyphs">THE</text>
      <text x="125" y="790" font-size="190" textLength="565" lengthAdjust="spacingAndGlyphs">HOLLOWING</text>
    </svg>

    <p class="writers">Written by Arlo Penning and Felix Dunmore</p>
  </main>
</body>
</html>
```